Electrical contracting business specialising in smoke detector installation needs flyer design

i need a flyer design made up highlighting the fact that the Qld legislation is changing on smoke detectors in homes for everyones safety. I am an electrical contractor ( Tandrell Electrical) specialising in smoke detector installation to comply with the new Qld legislation. Some of the wording that can be used-
When you sleep, your sense of smell also sleeps. If a fire starts, toxic fumes canovercome you. Photoelectric smoke alarms see smoke and will alert you early, so you can escape. With interconnected alarms, you will be alerted no matter where you are, or where the fire starts.
New legislation specifies the type, positioning and interconnectedness of alarms, which are critical factors for an early warning and a quick escape.
To give your family the best chance of surviving a house fire, update your smoke alarms to match the new legislation as soon as you can. Call ME on 0418362957

Target Market(s)

Body Corporates , people selling and renting their properties

Industry/Entity Type

Electrician

Colors

Designer to choose colors to be used in the design.

Requirements
Must have
• Safety aspect.

```html
<!DOCTYPE html>
<html lang="en">
<head>
<meta charset="utf-8">
<title>Tandrell Electrical – Smoke Alarm Flyer</title>
<link rel="stylesheet" href="https://fonts.googleapis.com/css2?family=Source+Sans+3:ital,wght@0,400;0,600;1,400;1,600&display=swap">
<style>
:root{
  --yellow:#f2c500;
  --dark:#3a3a3c;
  --hero:#4a4a4d;
  --ink:#4a4a4a;
  --paper:#ffffff;
  --bg:#e9e7e4;
}
*{box-sizing:border-box;margin:0;padding:0}
html,body{width:1200px;height:891px;overflow:hidden;background:var(--bg)}
body{font-family:"Source Sans 3",sans-serif;color:var(--ink);position:relative}
.sheet{position:absolute;top:77px;width:595px;height:842px;background:var(--paper);transform:scale(.874);transform-origin:0 0;box-shadow:0 4px 14px rgba(0,0,0,.25);overflow:hidden}
.sheet--front{left:60px}
.sheet--back{left:620px}
.abs{position:absolute}
/* header */
.brand{left:25px;top:32px;display:flex;align-items:center;gap:10px}
.brand__mark{width:26px;height:26px;background:var(--dark)}
.brand__name{font-size:19px;line-height:1.1;color:#333;font-weight:400}
.agency{left:312px;top:36px;width:283px;height:28px;background:var(--yellow);clip-path:polygon(8px 0,100% 0,100% 100%,0 100%);font-size:13px;color:#222;display:flex;align-items:center;padding-left:18px}
/* hero */
.hero{left:0;top:97px;width:595px;height:196px;background:var(--hero)}
.hero__photo{position:absolute;top:0;height:196px}
.sheet--front .hero__photo{right:0;width:320px;background:linear-gradient(135deg,#3b3226,#8a6a3e 55%,#2a241c);clip-path:polygon(70px 0,100% 0,100% 100%,0 100%)}
.sheet--back .hero__photo{left:0;width:320px;background:linear-gradient(160deg,#1c2430,#4f7c8e 45%,#6c6c70);clip-path:polygon(0 0,100% 0,250px 100%,0 100%)}
.hero__title{position:absolute;color:#fff;font-style:italic;font-size:19px;line-height:24px}
.sheet--front .hero__title{left:15px;top:45px}
.sheet--back .hero__title{right:18px;top:44px;text-align:right;font-size:22px;line-height:30px}
.alarm{border-radius:50%;background:radial-gradient(circle at 45% 40%,#ffffff,#d6d6d6 70%,#a9a9a9)}
/* columns */
.side{left:353px;top:316px;width:242px;height:526px;background:var(--dark);color:#fff;padding:0 8px}
.side h2{color:var(--yellow);font-weight:400;font-size:15px;text-align:center}
.side h3{font-weight:400;font-size:10px;padding-bottom:5px;border-bottom:1px solid var(--yellow);display:inline-block;margin-bottom:8px}
.side p{font-size:10px;line-height:13px}
.ticks{list-style:none;font-size:7.6px;line-height:9px;margin-bottom:16px}
.ticks li{position:relative;padding-left:10px;margin-bottom:4px}
.ticks li::before{content:"✓";position:absolute;left:0;top:0;width:6px;height:6px;border:1px solid var(--yellow);border-radius:50%;color:var(--yellow);font-size:5px;line-height:5px;text-align:center}
.copy{left:15px;width:315px;font-size:10.5px;line-height:13.5px;text-align:justify}
.copy p{margin-bottom:14px}
.note{font-size:8px}
.band{left:0;height:28px;background:var(--yellow);color:#fff;font-size:16px;display:flex;align-items:center;padding-left:14px;clip-path:polygon(0 0,100% 0,calc(100% - 12px) 100%,0 100%)}
.callout{left:15px;top:672px;width:315px;height:68px;border-left:1px dashed #ccc;border-right:1px dashed #ccc;font-size:10.5px;line-height:17px;text-align:center;padding-top:8px}
.rule{left:0;top:750px;width:343px;height:7px;background:var(--yellow)}
.contact{left:14px;top:778px;font-size:11px;color:#222}
.phone{left:16px;top:799px;width:185px;height:28px;background:var(--dark);clip-path:polygon(0 0,100% 0,calc(100% - 8px) 100%,0 100%);display:flex;align-items:center;gap:8px;padding-left:6px;color:var(--yellow);font-size:16px;font-weight:600}
.badges{right:12px;top:770px;display:flex;gap:14px}
.badge{width:46px;height:52px;background:#cfcfcf}
.badge--round{border-radius:50%;background:#b5242b;height:46px;margin-top:6px}
</style>
</head>
<body>

<section class="sheet sheet--front">
  <div class="abs brand"><span class="brand__mark"></span><span class="brand__name">Tandrell Electrical</span></div>
  <div class="abs agency">Regional Fire and Emergency Services</div>

  <div class="abs hero">
    <div class="hero__photo" role="img" aria-label="Night photo of a stone house with lit windows"></div>
    <p class="hero__title">When you sleep,<br>your sense of smell also sleeps.<br>If a fire starts, toxic fumes can<br>over come you.</p>
  </div>

  <div class="abs side">
    <h2 style="margin-top:86px">New Smoke Alarm Legislation</h2>
    <h3 style="margin-top:24px">Smoke alarms in all dwellings must:</h3>
    <ul class="ticks">
      <li>Be photoelectric (as 3786-2014)</li>
      <li>Not also contain an ionisation sensor</li>
      <li>Be less than 10 years old</li>
      <li>Operate when tested</li>
      <li>Be interconnected with every other smoke alarm in the dwelling so all activate together</li>
    </ul>
    <h3>Smoke alarms must be installed on each storey:</h3>
    <ul class="ticks">
      <li>In each bedroom</li>
      <li>In hallways which connect bedrooms and the rest of the dwelling</li>
      <li>If there is no hallway, between the bedrooms and other parts of the storey</li>
      <li>If there are no bedrooms on a storey at least one smoke alarm must be installed in the most likely path of travel to exit the dwelling.</li>
    </ul>
    <p>Smoke alarms must be either hardwired or powered by a nonremovable 10-year battery.</p>
  </div>
  <div class="abs alarm" style="left:395px;top:230px;width:175px;height:140px" role="img" aria-label="White ceiling smoke alarm"></div>

  <div class="abs copy" style="top:315px">
    <p>Photoelectric smoke alarms see smoke and will alert you early, so you can escape. With interconnected alarms, you will be alerted no matter where you are, or where the fire starts.</p>
    <p>New legislation specifies the type, positioning and interconnectedness of alarms, which are critical factors for an early warning and a quick escape.</p>
    <p>To give your family the best chance of surviving a house fire, update your smoke alarms to match the new legislation as soon as you can.</p>
  </div>

  <div class="abs band" style="top:500px;width:287px">Replacing smoke alarms</div>

  <div class="abs copy" style="top:547px">
    <p>Existing smoke alarms manufactured more than ten years ago must be replaced.<br><span class="note">(Note: Smoke alarms should have the date of manufacture stamped on them.)</span></p>
    <p>Smoke alarms that do not operate when tested must be replaced immediately. Existing hardwired smoke alarms that need replacement must be replaced with a hardwired smoke alarm.</p>
  </div>
  <div class="abs callout">When replacing smoke alarms, they must be<br>of a photoelectric type which complies with<br>Australian Standard (AS) 3786-2014.</div>

  <div class="abs rule"></div>
  <p class="abs contact">FOR MORE INFORMATION PLEASE CONTACT US</p>
  <div class="abs phone">
    <svg width="18" height="18" viewBox="0 0 18 18" aria-hidden="true"><circle cx="9" cy="9" r="8" fill="none" stroke="#f2c500" stroke-width="1.5"/><path d="M6 5l2 2-1 1.2c.6 1.2 1.6 2.2 2.8 2.8L11 10l2 2-1.2 1.2C8.5 13 5 9.5 4.8 6.2z" fill="#f2c500"/></svg>
    0418362957
  </div>
  <div class="abs badges"><span class="badge badge--round"></span><span class="badge"></span></div>
</section>

<section class="sheet sheet--back">
  <div class="abs brand"><span class="brand__mark"></span><span class="brand__name">Tandrell Electrical</span></div>
  <div class="abs agency">Regional Fire and Emergency Services</div>

  <div class="abs hero">
    <div class="hero__photo" role="img" aria-label="Child's bedroom at night with smoke alarm sensing beams"></div>
    <p class="hero__title">Are you up to speed with<br>smoke alarms?</p>
  </div>
  <div class="abs alarm" style="left:478px;top:215px;width:104px;height:84px" role="img" aria-label="White ceiling smoke alarm"></div>

  <div class="abs band" style="top:316px;width:330px">Requirements as for existing dwellings.</div>
  <div class="abs copy" style="top:362px">
    <p>Existing landlord's and tenant's obligations regarding the installation and testing of smoke alarms continue.</p>
    <p>Property sellers must continue to lodge a Form 24 with the State Land Registry Office stating the requirements of the smoke alarm legislation have been met.</p>
    <p>The development approval process for new dwellings and substantial renovations will ensure that building approvals received on or after this date will bring dwellings into compliance with the new laws.</p>
  </div>

  <div class="abs band" style="top:555px;width:330px;font-size:14px">Prescribed locations for installing smoke alarms</div>
  <div class="abs copy" style="top:593px">
    <p>There are special requirements for stairways, sloping ceilings, and ceilings with exposed beams. Specific requirements will be explained in the Building Fire Safety Regulation 2008.</p>
    <p>If impractical for the prescribed location requirements to be met (e.g. may be affected by steam from shower or fumes from cooking), the owner may put the alarm at another location that will provide a warning to occupants of the dwelling.</p>
  </div>

  <div class="abs side">
    <h2 style="margin-top:12px">New Smoke Alarm Legislation</h2>
    <h3 style="margin-top:10px">Smoke alarms in all dwellings must:</h3>
    <ul class="ticks">
      <li>Be photoelectric (as 3786-2014)</li>
      <li>Not also contain an ionisation sensor</li>
      <li>Be less than 10 years old</li>
      <li>Operate when tested</li>
      <li>Be interconnected with every other smoke alarm in the dwelling so all activate together</li>
    </ul>
    <h3>Smoke alarms must be installed on each storey:</h3>
    <ul class="ticks">
      <li>In each bedroom</li>
      <li>In hallways which connect bedrooms and the rest of the dwelling</li>
      <li>If there is no hallway, between the bedrooms and other parts of the storey</li>
      <li>If there are no bedrooms on a storey at least one smoke alarm must be installed in the most likely path of travel to exit the dwelling.</li>
    </ul>
    <p style="margin-bottom:22px">Smoke alarms must be either hardwired or powered by a nonremovable 10-year battery.</p>
    <p style="margin-bottom:12px">Where practicable smoke alarms must be placed on the ceiling. Smoke alarms must not be placed:</p>
    <ul class="ticks">
      <li>Within 300mm of a corner of a ceiling and a wall</li>
      <li>Within 300mm of a light fitting</li>
      <li>Within 400mm of an air-conditioning vent</li>
      <li>Within 400mm of the blades of a ceiling fan</li>
    </ul>
  </div>

  <div class="abs rule"></div>
  <p class="abs contact">FOR MORE INFORMATION PLEASE CONTACT US</p>
  <div class="abs phone">
    <svg width="18" height="18" viewBox="0 0 18 18" aria-hidden="true"><circle cx="9" cy="9" r="8" fill="none" stroke="#f2c500" stroke-width="1.5"/><path d="M6 5l2 2-1 1.2c.6 1.2 1.6 2.2 2.8 2.8L11 10l2 2-1.2 1.2C8.5 13 5 9.5 4.8 6.2z" fill="#f2c500"/></svg>
    0418362957
  </div>
  <div class="abs badges"><span class="badge badge--round"></span><span class="badge"></span></div>
</section>

</body>
</html>
```